Town Wordpress Design Project

Hi,
I am looking for someone to completely start from scratch on a website for a town in Texas named Brindowvale. I designed their last website about 4 years ago but am not able to give them what I would like to with my abilities. I need a wordpress website that is web 2.0 in design while still being creative. Their current website can be seen at www.brindowvale.us. They like such websites by a company named Marvenlo, you can view their town website portfolio here: http://www.marvenlo.com/index.aspx?NID=137. I would need all of the pages and info that is on their current site to be moved to the new site that I am hoping you can create for me. I want a much cleaner, nicer, and simpler navigation panel, while hiding links in drop down menus. I also want to include a calendar where they could post upcoming events and would want them to be able to add submit-able forms whenever they would need to. A search option would also be nice. I know that this is a design community, but if you could code the site as well or know someone who can, please let me know. Their Town Logo can be found attached, and the font in which you spell out their town name is totally up to you. They want their Agenda and Minutes to display like this: http://www.qwobel.com/index.aspx?NID=266. Let me know if you have any further questions...
If at all possible, I wouldn't mind the design to be designed in such a way that making it "responsive" someday would be easily possible...
Reason: More time needed for some designers...
Reason: Additional time needed...

```html
<!DOCTYPE html>
<html lang="en">
<head>
<meta charset="utf-8">
<title>Town of Brindowvale</title>
<link href="https://fonts.googleapis.com/css2?family=Roboto+Condensed:wght@400;700&family=Arimo:wght@400;700&display=swap" rel="stylesheet">
<style>
:root{
  --red:#c40f33;
  --navy:#0b2a6e;
  --ink:#111;
  --text:#2b2b2b;
  --grey:#e9e9e9;
  --line:#d6d6d6;
  --orange:#f2a000;
}
*{box-sizing:border-box;margin:0;padding:0}
html,body{width:919px;height:1200px;overflow:hidden}
body{position:relative;background:#fff;font-family:Arimo,Arial,sans-serif;color:var(--text)}

/* header */
.masthead{position:absolute;left:0;top:0;width:919px;height:139px;background:#fff}
.nav-bars{position:absolute;left:150px;top:28px;width:737px;height:88px;border-radius:0 34px 34px 0;overflow:hidden}
.bar{position:absolute;left:0;width:100%;font-family:"Roboto Condensed",Arial Narrow,sans-serif;color:#fff}
.bar-quick{top:0;height:28px;background:var(--navy);font-size:12.5px;line-height:28px;padding-left:4px}
.bar-main{top:28px;height:30px;background:var(--ink);font-size:15px;line-height:30px}
.bar-sub{top:58px;height:30px;background:var(--red);font-size:12.5px;line-height:30px}
.bar span{position:absolute;white-space:nowrap}
.pill{background:var(--red);border-radius:13px;padding:0 8px;line-height:22px;top:4px}
.request{position:absolute;left:602px;top:34px;height:18px;padding:0 9px;border-radius:9px;background:var(--red);color:#fff;font:12.5px/18px "Roboto Condensed",sans-serif}
.search{position:absolute;left:727px;top:33px;width:140px;height:20px;border-radius:10px;background:#fff;border:1px solid #c9c9c9;font-size:9px;line-height:18px;padding-left:10px;color:#555}
.search svg{position:absolute;right:7px;top:3px}
.seal{position:absolute;left:33px;top:12px;width:120px;height:120px;border-radius:50%;background:#fff;border:5px solid var(--ink);display:flex;align-items:center;justify-content:center;font:700 14px "Roboto Condensed",sans-serif;color:var(--ink)}

/* hero */
.rule{position:absolute;left:0;width:919px;background:var(--ink)}
.hero{position:absolute;left:0;top:145px;width:919px;height:412px;background:linear-gradient(180deg,#6e8a4c 0%,#8aa36a 35%,#9cae78 55%,#7f9a52 75%,#6d8a3f 100%)}
.hero-arrow{position:absolute;top:298px}
.dots{position:absolute;left:421px;top:528px;display:flex;gap:4px}
.dots i{display:block;width:12px;height:12px;border:2px solid #333;background:#555}
.dots i.on{border-color:var(--red);background:#fff;box-shadow:inset 0 0 0 2px var(--red)}

/* request popup */
.request-form{position:absolute;left:303px;top:67px;width:415px;height:236px;background:#fff;border-radius:4px;box-shadow:0 0 8px rgba(0,0,0,.45);font-size:9.8px}
.request-form::before{content:"";position:absolute;left:350px;top:-9px;border:9px solid transparent;border-top:0;border-bottom-color:#fff}
.request-form .intro{position:absolute;left:16px;top:13px;color:var(--red);line-height:15.4px}
.field label{position:absolute;font-weight:700;color:#333;font-size:9.8px}
.field label b{color:var(--red);font-weight:400}
.field .input{position:absolute;width:182px;height:21px;background:#ececec;border:1px solid #dadada}
.btn{position:absolute;top:197px;height:22px;line-height:22px;background:var(--red);color:#fff;font-weight:700;font-size:10.5px;text-align:center;border-radius:2px}
.close{position:absolute;left:707px;top:57px}

/* content */
.news h1{position:absolute;left:33px;top:575px;font:700 19px "Roboto Condensed",sans-serif;color:var(--red)}
.news .underline{position:absolute;left:33px;top:600px;width:275px;height:1px;background:linear-gradient(90deg,var(--red),rgba(196,15,51,0))}
.news h2{position:absolute;left:33px;top:611px;font-size:11.5px;font-weight:700;color:var(--ink)}
.news p{position:absolute;left:33px;top:630px;width:598px;font-size:10.3px;line-height:15.2px;text-align:justify;color:#333}

.boards{position:absolute;left:34px;top:729px;width:596px;border:1px solid var(--red);border-top:0}
.boards .row{display:flex;height:24.7px;align-items:center;font-size:10.4px;color:#222}
.boards .row:nth-child(odd){background:#ebebeb}
.boards .row.head{height:29px;background:var(--red);color:#fff;font-weight:700;font-size:12px}
.boards .name{width:416px;padding-left:9px;height:100%;display:flex;align-items:center}
.boards .head .name{justify-content:center;padding:0}
.boards .col{height:100%;display:flex;align-items:center;justify-content:center;gap:14px;border-left:5px solid #fff;width:90px}

/* sidebar */
.side-box{position:absolute;left:648px;width:239px;border:1px solid var(--line);background:#fff}
.side-box h3{background:var(--grey);color:var(--red);font-size:11.2px;font-weight:700;padding:0 10px;height:27px;line-height:27px;white-space:nowrap}
.side-box ul{list-style:none;padding:4px 4px 4px 10px}
.side-box li{position:relative;padding-left:17px;font-size:10.2px;line-height:20.5px;color:#333;white-space:nowrap;letter-spacing:-.1px}
.side-box li.wrap{white-space:normal}
.side-box li svg{position:absolute;left:0;top:4px}
.event{margin:0 10px;padding:8px 0 7px;border-bottom:1px dashed #bbb;font-size:10.3px;color:#333}
.event:last-child{border-bottom:0}
.event strong{display:block;color:var(--ink);margin-bottom:3px}
.event p{line-height:15.4px;text-align:justify}

/* footer */
.site-footer{position:absolute;left:0;top:1126px;width:919px;height:74px;background:var(--grey);font-size:10.5px;color:#333}
.site-footer .copy{position:absolute;left:33px;top:10px}
.badge{position:absolute;top:33px;height:27px;border:1px solid #5a6ea3;background:#fff;color:var(--navy);display:flex;align-items:center}
.badge-social{left:33px;width:82px;padding-left:6px;gap:5px;font-size:8px;line-height:9px}
.badge-social i{display:block;width:14px;height:14px;background:var(--navy)}
.badge-social b{font-size:11px;font-weight:700;display:block;line-height:12px}
.badge-bills{left:124px;width:102px;justify-content:center;font-size:12.5px}
.contact{position:absolute;right:32px;top:10px;text-align:right;line-height:17px}
.contact b{color:#222}
</style>
</head>
<body>

<svg width="0" height="0" style="position:absolute">
  <defs>
    <symbol id="star" viewBox="0 0 20 20"><path d="M10 1l2.6 5.6 6.1.7-4.5 4.2 1.2 6.1L10 14.6 4.6 17.6l1.2-6.1L1.3 7.3l6.1-.7z" fill="#f2a000" stroke="#d88400" stroke-width=".8"/></symbol>
    <symbol id="plus" viewBox="0 0 20 20"><path d="M8 2h4v6h6v4h-6v6H8v-6H2V8h6z" fill="#f5a500"/></symbol>
    <symbol id="doc" viewBox="0 0 12 13"><path d="M1 1h7l3 3v8H1z" fill="#fff" stroke="#bbb" stroke-width=".8"/><rect x="0" y="3" width="7" height="6" fill="#d21f2a"/></symbol>
  </defs>
</svg>

<header class="masthead">
  <div class="nav-bars">
    <div class="bar bar-quick">&nbsp;Quick links: Latest News &amp; Events | FAQ's | Online Payments</div>
    <div class="bar bar-main">
      <span class="pill" style="left:6px">My Brindowvale</span>
      <span style="left:124px">Police Department</span>
      <span style="left:577px">Commissions</span>
      <span style="left:665px">Contact Us</span>
    </div>
    <div class="bar bar-sub">
      <span style="left:4px">Forms &amp; Applications | Related Links</span>
      <span style="left:546px">Permitted Gas Wells</span>
    </div>
  </div>
  <div class="request">Request Information</div>
  <div class="search">Search
    <svg width="13" height="13" viewBox="0 0 13 13"><circle cx="5.5" cy="5.5" r="4" fill="none" stroke="#555" stroke-width="1.6"/><path d="M8.5 8.5l3.5 3.5" stroke="#555" stroke-width="1.8"/></svg>
  </div>
  <div class="seal">Brindowvale</div>
</header>

<div class="rule" style="top:139px;height:6px"></div>
<div class="hero" role="img" aria-label="Photo of riders on horses and cattle on a green meadow in front of farm buildings"></div>
<div class="rule" style="top:557px;height:4px"></div>
<svg class="hero-arrow" style="left:34px" width="26" height="88" viewBox="0 0 26 88"><path d="M24 2L3 44l21 42" fill="none" stroke="#c40f33" stroke-width="3"/></svg>
<svg class="hero-arrow" style="left:860px" width="26" height="88" viewBox="0 0 26 88"><path d="M2 2l21 42L2 86" fill="none" stroke="#c40f33" stroke-width="3"/></svg>
<div class="dots"><i class="on"></i><i></i><i></i><i></i><i></i></div>

<form class="request-form">
  <p class="intro">Want to know more? Fill out the form and we'll get you all the information you need!<br>Can't wait to get started? Give us a call so we can talk with you directly,</p>
  <div class="field"><label style="left:16px;top:59px">Name: <b>*</b></label><div class="input" style="left:16px;top:70px"></div></div>
  <div class="field"><label style="left:216px;top:59px">Position / Title:</label><div class="input" style="left:216px;top:70px"></div></div>
  <div class="field"><label style="left:16px;top:106px">Email Address: <b>*</b></label><div class="input" style="left:16px;top:117px"></div></div>
  <div class="field"><label style="left:216px;top:106px">Phone: <b>*</b></label><div class="input" style="left:216px;top:117px"></div></div>
  <div class="field"><label style="left:16px;top:153px">Organization Name: <b>*</b></label><div class="input" style="left:16px;top:164px"></div></div>
  <div class="field"><label style="left:216px;top:153px">Existing Website Address:</label><div class="input" style="left:216px;top:164px"></div></div>
  <div class="btn" style="left:297px;width:48px">Submit</div>
  <div class="btn" style="left:351px;width:47px">Cancel</div>
</form>
<svg class="close" width="18" height="18" viewBox="0 0 18 18"><circle cx="9" cy="9" r="8" fill="#c40f33" stroke="#fff" stroke-width="1.5"/><path d="M5.5 5.5l7 7M12.5 5.5l-7 7" stroke="#fff" stroke-width="2.2"/></svg>

<section class="news">
  <h1>What is Happening in Brindowvale?</h1>
  <div class="underline"></div>
  <h2>Neighborhood Night Out Event in Brindowvale on Tuesday, October 2nd.</h2>
  <p>Please reserve this date on your calendar! Come out and participate in a Neighborhood Night Out event at Town Hall on Tuesday, October 2nd. This event will be held in participation with the Merrow County Sheriff's Department and include surrounding communities. Neighborhood Night Out is designed to heighten crime and drug prevention awareness; generate support for, and participation in, local anti-crime programs; strengthen neighborhood spirit and police-community partnerships; and send a message to criminals letting them know that neighborhoods are organized and fighting back. More details to follow soon.</p>
</section>

<div class="boards">
  <div class="row head"><div class="name">Board</div><div class="col">Agendas</div><div class="col">Minutes</div></div>
  <div class="row"><div class="name">Animal Shelter Advisory Board</div><div class="col"><svg width="15" height="15"><use href="#star"/></svg><svg width="15" height="15"><use href="#plus"/></svg></div><div class="col"><svg width="15" height="15"><use href="#star"/></svg><svg width="15" height="15"><use href="#plus"/></svg></div></div>
  <div class="row"><div class="name">Capital Improvement Advisory Committee</div><div class="col"><svg width="15" height="15"><use href="#star"/></svg><svg width="15" height="15"><use href="#plus"/></svg></div><div class="col"><svg width="15" height="15"><use href="#star"/></svg><svg width="15" height="15"><use href="#plus"/></svg></div></div>
  <div class="row"><div class="name">Capital Improvement Projects (CIP) Committee</div><div class="col"><svg width="15" height="15"><use href="#star"/></svg><svg width="15" height="15"><use href="#plus"/></svg></div><div class="col"><svg width="15" height="15"><use href="#star"/></svg><svg width="15" height="15"><use href="#plus"/></svg></div></div>
  <div class="row"><div class="name">City Council</div><div class="col"><svg width="15" height="15"><use href="#star"/></svg><svg width="15" height="15"><use href="#plus"/></svg></div><div class="col"><svg width="15" height="15"><use href="#star"/></svg><svg width="15" height="15"><use href="#plus"/></svg></div></div>
  <div class="row"><div class="name">Civil Service Commission</div><div class="col"><svg width="15" height="15"><use href="#star"/></svg><svg width="15" height="15"><use href="#plus"/></svg></div><div class="col"><svg width="15" height="15"><use href="#star"/></svg><svg width="15" height="15"><use href="#plus"/></svg></div></div>
  <div class="row"><div class="name">Construction Code Appeals Board</div><div class="col"><svg width="15" height="15"><use href="#star"/></svg><svg width="15" height="15"><use href="#plus"/></svg></div><div class="col"><svg width="15" height="15"><use href="#star"/></svg><svg width="15" height="15"><use href="#plus"/></svg></div></div>
  <div class="row"><div class="name">Crime Control &amp; Prevention District Board</div><div class="col"><svg width="15" height="15"><use href="#star"/></svg><svg width="15" height="15"><use href="#plus"/></svg></div><div class="col"><svg width="15" height="15"><use href="#star"/></svg><svg width="15" height="15"><use href="#plus"/></svg></div></div>
  <div class="row"><div class="name">Economic Development Advisory Committee</div><div class="col"><svg width="15" height="15"><use href="#star"/></svg><svg width="15" height="15"><use href="#plus"/></svg></div><div class="col"><svg width="15" height="15"><use href="#star"/></svg><svg width="15" height="15"><use href="#plus"/></svg></div></div>
  <div class="row"><div class="name">Gas Board of Appeals</div><div class="col"><svg width="15" height="15"><use href="#star"/></svg><svg width="15" height="15"><use href="#plus"/></svg></div><div class="col"><svg width="15" height="15"><use href="#star"/></svg><svg width="15" height="15"><use href="#plus"/></svg></div></div>
  <div class="row"><div class="name">Keep BV Beautiful Commission</div><div class="col"><svg width="15" height="15"><use href="#star"/></svg><svg width="15" height="15"><use href="#plus"/></svg></div><div class="col"><svg width="15" height="15"><use href="#star"/></svg><svg width="15" height="15"><use href="#plus"/></svg></div></div>
  <div class="row"><div class="name">Eastfield Transit Service (ETS) Board</div><div class="col"><svg width="15" height="15"><use href="#star"/></svg><svg width="15" height="15"><use href="#plus"/></svg></div><div class="col"><svg width="15" height="15"><use href="#star"/></svg><svg width="15" height="15"><use href="#plus"/></svg></div></div>
  <div class="row"><div class="name">Park &amp; Recreation Facilities Development Corp. Board</div><div class="col"><svg width="15" height="15"><use href="#star"/></svg><svg width="15" height="15"><use href="#plus"/></svg></div><div class="col"><svg width="15" height="15"><use href="#star"/></svg><svg width="15" height="15"><use href="#plus"/></svg></div></div>
  <div class="row"><div class="name">Eastfield Transit Service (ETS) Board</div><div class="col"><svg width="15" height="15"><use href="#star"/></svg><svg width="15" height="15"><use href="#plus"/></svg></div><div class="col"><svg width="15" height="15"><use href="#star"/></svg><svg width="15" height="15"><use href="#plus"/></svg></div></div>
  <div class="row"><div class="name">Park &amp; Recreation Facilities Development Corp. Board</div><div class="col"><svg width="15" height="15"><use href="#star"/></svg><svg width="15" height="15"><use href="#plus"/></svg></div><div class="col"><svg width="15" height="15"><use href="#star"/></svg><svg width="15" height="15"><use href="#plus"/></svg></div></div>
</div>

<aside class="side-box" style="top:579px;height:295px">
  <h3>2011 Annual Drinking Water Quality Report</h3>
  <ul><li><svg width="11" height="12"><use href="#doc"/></svg>2011 Report</li></ul>
  <h3>Water Conservation</h3>
  <ul><li><svg width="11" height="12"><use href="#doc"/></svg>2011 Property Tax Rates</li></ul>
  <h3>Misc. Information</h3>
  <ul>
    <li><svg width="11" height="12"><use href="#doc"/></svg>2010 Annual Drinking Water Quality Report</li>
    <li><svg width="11" height="12"><use href="#doc"/></svg>Approved Budget for FY 2010-2011</li>
    <li><svg width="11" height="12"><use href="#doc"/></svg>Municipal Energy Usage Report</li>
    <li><svg width="11" height="12"><use href="#doc"/></svg>2009 Annual Drinking Water Quality Report</li>
    <li><svg width="11" height="12"><use href="#doc"/></svg>Planning &amp; Zoning Commission and Board<br>of Adjustment Application</li>
    <li><svg width="11" height="12"><use href="#doc"/></svg>Water Conservation Plan</li>
  </ul>
</aside>

<aside class="side-box" style="top:887px;height:220px">
  <h3>Events</h3>
  <div class="event"><strong>Wed, 26 Sep&nbsp; To&nbsp; Sat, 29 Sep</strong><p>Lorem Ipsum is simply dummy text of the printing and typesetting industry.</p></div>
  <div class="event"><strong>Wed, 26 Sep&nbsp; To&nbsp; Sat, 29 Sep</strong><p>Lorem Ipsum is simply dummy text of the printing and typesetting industry.</p></div>
  <div class="event"><strong>Wed, 26 Sep&nbsp; To&nbsp; Sat, 29 Sep</strong><p>Lorem Ipsum is simply dummy text of the printing and typesetting industry.</p></div>
</aside>

<footer class="site-footer">
  <div class="copy">Copyright @ 2012-2013 brindowvaletexas. All Rights Reserved</div>
  <div class="badge badge-social"><i></i><span>Find us on<b>Chatterly</b></span></div>
  <div class="badge badge-bills">View / Pay e-Bills</div>
  <div class="contact"><b>Call:</b> 555-014-2290<br><b>Address:</b> 4120 Harlow Creek Rd.<br>Brindowvale, TX 70000</div>
</footer>

</body>
</html>
```